Book Cover for 'Mira Kept the Lamp'

I need a book cover for my novel. The story is set in the ancient Greece of Dorelos, and is a retelling of a story from the Varenid. Clytemnestra's husband, Agamemnon, is the paramount king in Greece. When his sister in law Helen runs away to Troy with Paris, Agamemnon summons the Greek army to attack Troy and win her back. To ensure the right winds blow for his fleet to sail to Troy, Agamemnon sacrifices his eldest daughter. Clytemnestra takes revenge by murdering Agamemnon when he returns from conquering Troy. She is in turn murdered by their son Orestes a few years later to avenge his father's death.

I would like a cover which reflects the ancient Greek setting - I wondered whether a motif based on the artwork found on ancient Greek pottery might be appropriate, but I am open to other suggestions. Although the core of the story involve the daughter's murder, and the revenge killing of her husband, this is Clytemnestra's story and I want to present her as a great queen who rules a kingdom well in her husband's absence. The tradition in Greece was for women to be sequestered, but Clytemnestra comes from Sparta, a kingdom with greater freedom for women and a greater respect for them.

Although the time period and story are very different from my first novel, I would like this cover to convey that my latest book is by the same author and part of an ongoing body of work so that there is a sort of brand recognition. So some common denominator would be good

```html
<!DOCTYPE html>
<html lang="en">
<head>
<meta charset="utf-8">
<title>Mira Kept the Lamp — Book Cover</title>
<link rel="stylesheet" href="https://fonts.googleapis.com/css2?family=Amatic+SC:wght@700&family=Cinzel:wght@600&display=swap">
<style>
  :root {
    --page-bg: #ffffff;
    --parchment-light: #f1e6cf;
    --parchment-mid: #e6d6b6;
    --parchment-dark: #d2bd97;
    --stone-light: #e6e8dc;
    --stone-mid: #d3d5c6;
    --smoke: #a39682;
    --frieze-light: #dcd9cc;
    --frieze-dark: #b9b4a5;
    --frieze-line: #f4f2ea;
    --gold-light: #e9b86a;
    --gold-dark: #b27a2e;
    --blood: #b0101a;
    --ink: #141210;
  }
  * { margin: 0; padding: 0; box-sizing: border-box; }
  html, body {
    width: 1200px;
    height: 1059px;
    overflow: hidden;
    background: var(--page-bg);
  }
  .canvas { position: relative; width: 1200px; height: 1059px; }
  .book-cover {
    position: absolute;
    left: 280px;
    top: 40px;
    width: 640px;
    height: 980px;
    background:
      radial-gradient(ellipse at 25% 15%, var(--parchment-light) 0%, transparent 60%),
      radial-gradient(ellipse at 80% 90%, var(--parchment-dark) 0%, transparent 55%),
      var(--parchment-mid);
    box-shadow: 0 2px 10px rgba(0,0,0,0.18);
    overflow: hidden;
  }
  .book-title {
    position: absolute;
    top: 58px;
    left: 30px;
    font-family: "Amatic SC", cursive;
    font-weight: 700;
    font-size: 84px;
    text-transform: uppercase;
    letter-spacing: 1px;
    line-height: 1;
    white-space: nowrap;
    color: var(--ink);
  }
  .stone-panel {
    position: absolute;
    top: 170px;
    left: 24px;
    width: 592px;
    height: 640px;
    border-radius: 30px;
    background: radial-gradient(ellipse at 50% 45%, var(--stone-light) 0%, var(--stone-mid) 70%, var(--smoke) 100%);
    box-shadow: 0 0 40px 26px rgba(163,150,130,0.75);
  }
  .frieze {
    position: absolute;
    left: 0;
    width: 100%;
    background: linear-gradient(180deg, var(--frieze-light), var(--frieze-dark));
    border-top: 4px solid var(--frieze-line);
    border-bottom: 3px solid var(--frieze-dark);
    opacity: 0.9;
  }
  .frieze-upper { top: 20px; height: 90px; opacity: 0.6; }
  .frieze-lower { top: 440px; height: 100px; }
  .laurel-crown {
    position: absolute;
    top: 230px;
    left: 70px;
    width: 452px;
    height: 120px;
    border-radius: 50% 50% 50% 50% / 30% 30% 70% 70%;
    background: radial-gradient(ellipse at 50% 70%, var(--gold-light) 0%, var(--gold-dark) 75%, transparent 100%);
    opacity: 0.85;
  }
  .blood-drops { position: absolute; top: 578px; left: 220px; }
  .author-name {
    position: absolute;
    top: 875px;
    left: 0;
    width: 100%;
    text-align: center;
    font-family: "Cinzel", serif;
    font-weight: 600;
    font-size: 42px;
    letter-spacing: 1px;
    color: var(--ink);
  }
</style>
</head>
<body>
  <main class="canvas">
    <section class="book-cover">
      <h1 class="book-title">Mira Kept the Lamp</h1>
      <div class="stone-panel">
        <div class="frieze frieze-upper" role="img" aria-label="Carved marble frieze with scrolling foliage"></div>
        <div class="laurel-crown" role="img" aria-label="Golden laurel wreath crown"></div>
        <div class="frieze frieze-lower" role="img" aria-label="Carved marble frieze with a row of rosettes"></div>
        <svg class="blood-drops" width="150" height="30" viewBox="0 0 150 30" aria-hidden="true">
          <ellipse cx="10" cy="12" rx="7" ry="5" fill="var(--blood)"/>
          <ellipse cx="88" cy="12" rx="8" ry="5" fill="var(--blood)"/>
          <ellipse cx="136" cy="17" rx="12" ry="8" fill="var(--blood)"/>
        </svg>
      </div>
      <p class="author-name">Corinna Vale</p>
    </section>
  </main>
</body>
</html>
```